Construction site, small core-flute signage design required

Each building site requires a small sign (approx A4) that has my logo, company name, PO BOX address, website and phone number. I need a professional looking design. Please see attached my logos, and examples.

```html
<!DOCTYPE html>
<html lang="en">
<head>
<meta charset="utf-8">
<title>Harbourline Certifiers – Site Sign</title>
<link href="https://fonts.googleapis.com/css2?family=Open+Sans:wght@700&family=Arimo:wght@400;700&display=swap" rel="stylesheet">
<style>
  :root {
    --backdrop: #dedfe1;
    --brand-blue: #2081be;
    --navy: #2c3e50;
    --paper: #ffffff;
    --rule: #111111;
  }
  * { box-sizing: border-box; margin: 0; padding: 0; }
  html, body {
    width: 1200px; height: 896px; overflow: hidden;
    background: var(--backdrop);
  }
  .sign {
    position: absolute; left: 126px; top: 119px;
    width: 914px; height: 646px;
    background: var(--paper);
    font-family: "Open Sans", sans-serif;
  }
  .sign__header {
    position: absolute; left: 0; top: 0; width: 100%; height: 72px;
    background: var(--brand-blue);
    color: var(--paper);
    font-weight: 700; font-size: 44px; line-height: 72px;
    text-align: center; letter-spacing: 0.2px;
  }
  .sign__header-rule {
    position: absolute; left: 0; top: 72px; width: 100%; height: 10px;
    background: var(--navy);
  }
  .brand {
    position: absolute; left: 61px; top: 110px;
    display: flex; align-items: center; gap: 22px;
  }
  .brand__square {
    width: 88px; height: 88px; border-radius: 10px;
    background: var(--brand-blue);
  }
  .brand__name {
    font-weight: 700; font-size: 58px; color: var(--navy);
    letter-spacing: -1px; line-height: 1;
  }
  .field {
    position: absolute; left: 62px; width: 780px; height: 40px;
  }
  .field__label {
    position: absolute; left: 0; bottom: 6px;
    font-weight: 700; font-size: 27px; color: var(--navy); line-height: 1;
  }
  .field__line {
    position: absolute; left: 171px; right: 0; bottom: 0;
    height: 2px; background: var(--rule);
  }
  .field--cert { top: 258px; }
  .field--builder { top: 314px; }
  .field--licence { top: 369px; }
  .field--phone { top: 425px; }
  .notice {
    position: absolute; left: 0; top: 513px; width: 100%; height: 42px;
    background: var(--navy); color: var(--paper);
    font-family: "Arimo", sans-serif; font-weight: 700;
    font-size: 25px; line-height: 44px; text-align: center;
  }
  .contact {
    position: absolute; left: 0; top: 555px; width: 100%; height: 91px;
    background: var(--brand-blue); color: var(--paper);
    font-family: "Arimo", sans-serif; font-size: 18px;
  }
  .contact__row {
    position: absolute; left: 0; width: 100%;
    display: flex; justify-content: center; align-items: center; gap: 8px;
  }
  .contact__row--address { top: 15px; }
  .contact__row--links { top: 49px; gap: 0; }
  .contact__item { display: flex; align-items: center; gap: 11px; margin: 0 9px; }
  .contact__item--phone { font-weight: 700; }
  .icon { width: 21px; height: 21px; flex: none; }
</style>
</head>
<body>
  <div class="sign">
    <div class="sign__header">Principal Certifying Authority</div>
    <div class="sign__header-rule"></div>

    <div class="brand">
      <div class="brand__square"></div>
      <div class="brand__name">Harbourline Certifiers</div>
    </div>

    <div class="field field--cert"><span class="field__label">CC/CDC No:</span><span class="field__line"></span></div>
    <div class="field field--builder"><span class="field__label">BUILDER</span><span class="field__line"></span></div>
    <div class="field field--licence"><span class="field__label">LIC No:</span><span class="field__line"></span></div>
    <div class="field field--phone"><span class="field__label">Phone No:</span><span class="field__line"></span></div>

    <div class="notice">UNAUTHORISED ENTRY IS PROHIBITED</div>

    <div class="contact">
      <div class="contact__row contact__row--address">
        <svg class="icon" viewBox="0 0 21 21" fill="none" stroke="#fff" stroke-width="1.6">
          <rect x="1" y="1" width="19" height="19" rx="3"/>
          <path d="M10.5 16 C7.5 12 6.8 10.5 6.8 8.8 a3.7 3.7 0 0 1 7.4 0 c0 1.7 -0.7 3.2 -3.7 7.2z"/>
          <circle cx="10.5" cy="8.8" r="1.2"/>
        </svg>
        <span>18 Marlowe Rd, Coogee 2034, Sydney, NSW Australia</span>
      </div>
      <div class="contact__row contact__row--links">
        <span class="contact__item contact__item--phone">
          <svg class="icon" viewBox="0 0 21 21" fill="none" stroke="#fff" stroke-width="1.6">
            <rect x="1" y="1" width="19" height="19" rx="3"/>
            <path d="M6 6.5 l2-1 1.6 3 -1.3 1 c.8 1.6 1.6 2.4 3.2 3.2 l1-1.3 3 1.6 -1 2 c-4 .4 -8.9-4.5 -8.5-8.5z"/>
          </svg>
          (02) 9400 5172
        </span>
        <span class="contact__item">
          <svg class="icon" viewBox="0 0 21 21" fill="none" stroke="#fff" stroke-width="1.6">
            <rect x="1" y="1" width="19" height="19" rx="3"/>
            <rect x="5" y="6.5" width="11" height="8"/>
            <path d="M5 6.5 l5.5 4.5 5.5-4.5 M5 14.5 l4-3.5 M16 14.5 l-4-3.5"/>
          </svg>
          info@harbourlinecertifiers.com.au
        </span>
        <span class="contact__item">
          <svg class="icon" viewBox="0 0 21 21" fill="none" stroke="#fff" stroke-width="1.4">
            <rect x="1" y="1" width="19" height="19" rx="3"/>
            <circle cx="10.5" cy="10.5" r="5"/>
            <ellipse cx="10.5" cy="10.5" rx="2.2" ry="5"/>
            <path d="M5.5 10.5 h10"/>
          </svg>
          www.harbourlinecertifiers.com.au
        </span>
      </div>
    </div>
  </div>
</body>
</html>
```